Bayfield Tools and Building Materials Inc. (Rebranding)

Target Market(s)

mainly people who do DIY, and also construction companies.

Industry/Entity Type

Construction

Contact Information for Business Card

418 R. Malvar St. Brgy. 512 San Lazaro Manila, Philippines 1003
(02) 846-1937
www.btm-ph.com
bayfieldtools@mailbay.com

Number of Pages Required

5+ page

Font styles to use
Sans Serif

Colors
f37122
f78f20

Requirements
Must have
• to RETAIN the current logo used.
Nice to have
• ideas on how to apply the current logos to different promotional items
Should not have
• DO NOT change the Current Logo

```html
<!DOCTYPE html>
<html lang="en">
<head>
<meta charset="utf-8">
<title>Bayfield Tools and Building Materials Inc. – Business Card</title>
<link rel="stylesheet" href="https://fonts.googleapis.com/css2?family=Montserrat:wght@500;600;700;800&display=swap">
<style>
  :root {
    --orange: #f37122;
    --orange-light: #f78f20;
    --paper: #ffffff;
    --backdrop: #2f2f2f;
    --faint: #fdf0e6;
  }
  * { box-sizing: border-box; margin: 0; padding: 0; }
  html, body { width: 1200px; height: 829px; overflow: hidden; }
  body {
    position: relative;
    background: var(--backdrop);
    font-family: "Montserrat", sans-serif;
    color: var(--orange);
  }
  .card {
    position: absolute;
    background: var(--paper);
    overflow: hidden;
  }
  .card--front { left: 332px; top: 47px; width: 558px; height: 338px; }
  .card--back  { left: 336px; top: 437px; width: 557px; height: 336px; }

  .card__art { position: absolute; inset: 0; }

  .brand { position: absolute; display: flex; flex-direction: column; }
  .brand__row { display: flex; align-items: center; gap: 8px; }
  .brand__mark { width: 16px; height: 16px; background: var(--orange); }
  .brand__name {
    font-weight: 800;
    font-size: 38px;
    letter-spacing: -0.5px;
    line-height: 1;
    color: var(--orange);
  }
  .brand__tagline {
    font-weight: 500;
    font-size: 6.5px;
    letter-spacing: 0.6px;
    text-transform: uppercase;
    margin-top: 4px;
    color: var(--orange);
  }
  .card--front .brand { left: 34px; top: 58px; }
  .card--back .brand { left: 172px; top: 134px; }

  .holder { position: absolute; right: 43px; top: 42px; text-align: right; }
  .holder__name { font-weight: 700; font-size: 28px; line-height: 1; letter-spacing: 0.3px; }
  .holder__title { font-weight: 700; font-size: 13px; margin-top: 3px; letter-spacing: 0.3px; }

  .contacts { position: absolute; left: 32px; top: 217px; list-style: none; }
  .contacts li { font-weight: 600; font-size: 13px; line-height: 1; margin-bottom: 13px; }

  .footer-band {
    position: absolute; left: 0; right: 0; bottom: 0; height: 32px;
    background: var(--orange);
    color: var(--paper);
    font-weight: 700; font-size: 13px;
    display: flex; align-items: center; justify-content: center;
    letter-spacing: 0.3px;
  }
</style>
</head>
<body>

  <section class="card card--front" aria-label="Business card front">
    <svg class="card__art" width="558" height="338" viewBox="0 0 558 338" aria-hidden="true">
      <path d="M0 52 Q6 4 58 0 L0 0 Z" fill="var(--orange)"/>
      <polygon points="290,338 558,338 558,62" fill="var(--orange)"/>
      <polygon points="386,338 406,338 466,265 446,265" fill="var(--paper)"/>
      <polygon points="428,338 448,338 508,265 488,265" fill="var(--paper)"/>
      <polygon points="470,338 490,338 550,272 530,272" fill="var(--paper)"/>
      <polygon points="380,250 558,110 558,124 390,264" fill="var(--paper)"/>
    </svg>

    <div class="brand">
      <div class="brand__row">
        <span class="brand__mark"></span>
        <span class="brand__name">BAYFIELD</span>
      </div>
      <span class="brand__tagline">Tools and Building Materials Inc.</span>
    </div>

    <div class="holder">
      <p class="holder__name">YOUR NAME</p>
      <p class="holder__title">DIRECTOR</p>
    </div>

    <ul class="contacts">
      <li>ph: (02) 846-1937</li>
      <li>email: bayfieldtools@mailbay.com</li>
      <li>www.btm-ph.com</li>
    </ul>
  </section>

  <section class="card card--back" aria-label="Business card back">
    <svg class="card__art" width="557" height="336" viewBox="0 0 557 336">
      <defs>
        <linearGradient id="faintFade" x1="0" y1="0" x2="1" y2="1">
          <stop offset="0" stop-color="var(--faint)" stop-opacity="0.2"/>
          <stop offset="1" stop-color="var(--faint)"/>
        </linearGradient>
      </defs>
      <polygon role="img" aria-label="Faint brand decoration area" points="310,75 557,130 557,304 380,304" fill="url(#faintFade)"/>
    </svg>

    <div class="brand">
      <div class="brand__row">
        <span class="brand__mark"></span>
        <span class="brand__name">BAYFIELD</span>
      </div>
      <span class="brand__tagline">Tools and Building Materials Inc.</span>
    </div>

    <div class="footer-band">www.btm-ph.com</div>
  </section>

</body>
</html>
```